Service business needs Business Card Design

Looking to create a new business card design that is both professional and unique the can highlight the many services we offer throughout the seasons. Our tagline is "The Steadfast Touch"
Licensed & Insured: PA392617 has to be small and on the back side of the card.
On the Front:
FirstName LastName
Title
We offer the following services:
Deck Repair and Maintenance
Deck Cleaning and Staining/Painting
Power Washing/House Washing
Landscape Lighting Installation
Christmas Lighting Installation

```html
<!DOCTYPE html>
<html lang="en">
<head>
<meta charset="utf-8">
<title>Clearview Services – Business Card</title>
<link href="https://fonts.googleapis.com/css2?family=Montserrat:wght@400;500;600&family=Exo+2:wght@600&display=swap" rel="stylesheet">
<style>
  :root {
    --stage: #555555;
    --paper: #ffffff;
    --ink: #2b2b2b;
    --sky: #3aa8e0;
    --navy: #0f4c8a;
    --deep: #1b5f9e;
    --light: #52b5e4;
    --white: #ffffff;
  }
  * { margin: 0; padding: 0; box-sizing: border-box; }
  html, body { width: 900px; height: 1200px; overflow: hidden; }
  body {
    background: var(--stage);
    font-family: "Montserrat", Arial, sans-serif;
    position: relative;
  }
  .card {
    position: absolute;
    left: 79px;
    width: 743px;
    height: 441px;
    border-radius: 38px;
    box-shadow: 0 4px 6px rgba(0,0,0,0.55);
    overflow: hidden;
  }
  .card-front { top: 131px; background: var(--paper); }
  .card-back {
    top: 638px;
    background: linear-gradient(90deg, var(--deep) 0%, #2d7fbd 50%, var(--light) 100%);
    color: var(--white);
  }
  .brand {
    position: absolute;
    display: flex;
    align-items: center;
    gap: 14px;
    font-weight: 600;
    font-size: 34px;
    letter-spacing: 1px;
    line-height: 1.1;
  }
  .brand-name { display: block; }
  .brand-mark { width: 20px; height: 20px; flex: none; }
  .card-front .brand { left: 96px; top: 205px; color: var(--navy); }
  .card-front .brand-mark { background: var(--navy); }
  .card-back .brand { left: 92px; top: 168px; color: var(--white); }
  .card-back .brand-mark { background: var(--white); }

  .divider {
    position: absolute;
    left: 381px; top: 119px;
    width: 2px; height: 230px;
    background: var(--sky);
  }
  .contact { position: absolute; left: 414px; top: 113px; color: var(--ink); }
  .person-name {
    font-family: "Exo 2", Arial, sans-serif;
    font-weight: 600;
    font-size: 29px;
    color: var(--sky);
    letter-spacing: 0.5px;
    line-height: 1.1;
  }
  .person-title { font-size: 16px; margin-top: 1px; }
  .license { font-size: 16px; margin-top: 22px; }
  .license-label { color: var(--sky); font-weight: 500; }
  .contact-list { list-style: none; margin-top: 27px; }
  .contact-list li {
    display: flex; align-items: center; gap: 9px;
    font-size: 16px; height: 22.5px;
  }
  .contact-icon { width: 15px; height: 15px; flex: none; }
  .address { font-size: 16px; margin-top: 14px; line-height: 20px; }

  .services { position: absolute; left: 363px; top: 109px; }
  .services-heading { font-size: 19px; font-weight: 500; margin-bottom: 13px; }
  .service-list { list-style: none; margin-left: 5px; }
  .service-list li {
    font-size: 16.5px; height: 35px;
    display: flex; align-items: flex-start; gap: 10px;
  }
  .service-list li::before {
    content: ""; width: 7px; height: 7px; border-radius: 50%;
    background: var(--white); margin-top: 8px; flex: none;
  }
  .holiday-url { font-size: 16px; font-weight: 600; margin-left: 5px; margin-top: -1px; }
  .tagline {
    position: absolute; left: 0; right: 0; top: 370px;
    text-align: center; font-size: 21px; letter-spacing: 0.5px;
    text-transform: uppercase;
  }
</style>
</head>
<body>
  <section class="card card-front">
    <div class="brand"><span class="brand-mark"></span><span class="brand-name">Clearview<br>Services</span></div>
    <div class="divider"></div>
    <div class="contact">
      <h1 class="person-name">Marlo Pennick</h1>
      <p class="person-title">Owner</p>
      <p class="license"><span class="license-label">Licensed &amp; Insured:</span> PA392617</p>
      <ul class="contact-list">
        <li>
          <svg class="contact-icon" viewBox="0 0 16 16"><path fill="#3aa8e0" d="M2 6c0-2 3-3.5 6-3.5S14 4 14 6l-2.5 1L10 5.5H6L4.5 7Zm2 1.5L6 6h4l2 1.5V13H4Z"/></svg>
          555-014-2387
        </li>
        <li>
          <svg class="contact-icon" viewBox="0 0 16 16"><rect x="1.5" y="4" width="13" height="9" fill="#3aa8e0"/><path d="M1.5 4 8 9l6.5-5" fill="none" stroke="#fff" stroke-width="1.2"/></svg>
          info@clearviewservicesco.com
        </li>
        <li>
          <svg class="contact-icon" viewBox="0 0 16 16"><circle cx="8" cy="8" r="6.5" fill="#3aa8e0"/><path d="M5 4c2 1 1 3 3 3s1 3 0 4M10 3c0 2 2 2 3 3" fill="none" stroke="#fff" stroke-width="1.2"/></svg>
          www.clearviewservicesco.com
        </li>
      </ul>
      <p class="address">48 Harrow Lane, Suite 7<br>Elmford, PA 19022</p>
    </div>
  </section>

  <section class="card card-back">
    <div class="brand"><span class="brand-mark"></span><span class="brand-name">Clearview<br>Services</span></div>
    <div class="services">
      <h2 class="services-heading">We offer the following services</h2>
      <ul class="service-list">
        <li>Deck Repair and Maintenance</li>
        <li>Deck Cleaning and Staining/Painting</li>
        <li>Power Washing/House Washing</li>
        <li>Landscape Lighting Installation</li>
        <li>Christmas &amp; Holiday Light Installation</li>
      </ul>
      <p class="holiday-url">www.ClearviewHolidayLights.com</p>
    </div>
    <p class="tagline">The Steadfast Touch</p>
  </section>
</body>
</html>
```